Design for iOS app - Scanner App

We are developing an iOS app that is scanning receipts and mailing them to a predefined email address. The app should work more or less like TallySnap app (a short demo of the TallySnap app is available here: https://www.vidloomer.com/watch?v=QpRtWx83LmK).

We have prototyped the app in the link below:
http://app.framewisp.com/view/a71c3d02b58e9f46c1d7e0a2b94f8c5d

NB!: Please do not follow the mockups literally, but the Velmor Touch Layout Handbook!

The technical specifications and descriptions of the app's functionalities are available in the link below:
https://sheets.pallowdocs.com/document/d/7mPqo-RZ2xLwQbTfHaVk9YeNuJsDcX_3Pgtn4Hmcz5/edit?usp=sharing

Requirements for the design:

- The design should be provided as PSD, where each page/section should be in its own PSD file OR all pages/sections should be represented as folder groups in a single PSD file.

- All graphical elements in the design should be delivered as single layers which can then be extracted from the PSD.

- All graphical elements (icons, graphical buttons, etc.) should be provided as vector objects in the PSD, so that they can be exported into different sizes without loss of quality (for responsiveness).

- The design should use either web safe fonts or Google Fonts.

Instructions for the design:

The design should have habitual user interface like ordinary iOS navigation stack, with navigation bar on the top and all other elements on the bottom. That means just to make the top bar in your app be more like iOS. Please follow the Velmor Touch Layout Handbook, not the mockups literally .
FX: the e small elements in Dimensions screen like delete icons and active checkbox. In
https://devs.quorrelfield.com/library/mobile/documentation/UserExperience/Conceptual/TouchGuide/LayoutandAppearance.html#//ref/doc/uid/TX50017283-CH21-SW1
is described that interface elements should be at least 44x44 px - it's normal practice for all mobile development (iOS, android), so you should consider this too.

Please also provide an app icon and suggest a logo for the app.

Requirements
Must have
• Please make sure that the design is flat. Like iOS app, Pagelift, Tessivo apps etc.
Nice to have
• The design could be somewhat like the design for Brindlemark Pagelift(https://apps.quorrelstore.com/bg/app/brindlemark-pagelift/id451927730?mt=8) without being too similar
Should not have
• 3D look

```html
<!DOCTYPE html>
<html lang="en">
<head>
<meta charset="utf-8">
<title>Slipvault – Receipt Scanner App Screens</title>
<link rel="stylesheet" href="https://fonts.googleapis.com/css2?family=Roboto:wght@400;500;700&family=Montserrat:wght@700&display=swap">
<style>
  :root {
    --stage: #2b2b2b;
    --stage-light: #3a3a3a;
    --red: #e84c3d;
    --teal: #1bbc9b;
    --teal-dark: #16a085;
    --blue: #4dc3f5;
    --blue-dark: #2a8fb8;
    --grey-bar: #e2e2e2;
    --grey-field: #e8e8e8;
    --grey-panel: #dcdcdc;
    --text: #555;
    --text-light: #888;
    --white: #fff;
  }
  * { box-sizing: border-box; margin: 0; padding: 0; }
  html, body { width: 1113px; height: 1200px; overflow: hidden; }
  body {
    background: radial-gradient(ellipse at 50% 40%, var(--stage-light) 0%, var(--stage) 70%);
    font-family: "Roboto", Arial, sans-serif;
    color: var(--text);
    position: relative;
  }
  .screen {
    position: absolute;
    width: 206px;
    height: 410px;
    background: var(--white);
    overflow: hidden;
  }
  .caption {
    position: absolute;
    width: 250px;
    text-align: center;
    color: var(--white);
    font-size: 19px;
    font-weight: 400;
  }
  .nav-bar {
    height: 33px;
    background: var(--red);
    position: relative;
    display: flex;
    align-items: center;
    justify-content: center;
  }
  .app-name {
    font-family: "Roboto", Arial, sans-serif;
    font-weight: 700;
    font-size: 16px;
    color: var(--white);
  }
  .nav-left, .nav-right {
    position: absolute;
    top: 0; height: 33px;
    display: flex; align-items: center; gap: 8px;
  }
  .nav-left { left: 10px; }
  .nav-right { right: 10px; }
  .section-bar {
    height: 26px;
    background: var(--grey-bar);
    display: flex; align-items: center; gap: 6px;
    padding-left: 12px;
    font-size: 11px; font-weight: 500; color: #444;
  }
  .btn {
    display: flex; align-items: center; justify-content: center;
    height: 31px; margin: 0 14px;
    color: var(--white); font-size: 11px;
    border-bottom: 3px solid rgba(0,0,0,0.18);
  }
  .btn--blue { background: var(--blue); }
  .btn--teal { background: var(--teal); }
  .btn--red { background: var(--red); }
  .action-panel {
    position: absolute; left: 0; right: 0; bottom: 0;
    background: var(--grey-panel);
    display: flex; flex-direction: column; gap: 7px;
    padding-top: 8px;
  }

  /* Splash */
  .splash-photo {
    position: absolute; inset: 0;
    background: linear-gradient(160deg, #ea5446 0%, #e3463a 55%, #d63e33 100%);
  }
  .splash-brand {
    position: absolute; left: 0; right: 0; top: 190px;
    display: flex; flex-direction: column; align-items: center; gap: 6px;
  }
  .splash-name { display: flex; align-items: center; gap: 7px; }
  .splash-name .mark { width: 18px; height: 18px; border: 2px solid var(--white); }
  .splash-name .app-name { font-size: 26px; }
  .tagline { color: var(--white); font-size: 5px; letter-spacing: 0.5px; }

  /* Main */
  .scan-button {
    position: absolute; left: 55px; top: 109px;
    width: 96px; height: 96px; border-radius: 50%;
    background: var(--red);
    box-shadow: 0 0 0 4px var(--white), 0 0 0 7px var(--red);
    display: flex; align-items: center; justify-content: center; text-align: center;
    color: var(--white); font-family: "Montserrat", Arial, sans-serif;
    font-size: 12px; font-weight: 700; line-height: 1.1;
  }
  .status { position: absolute; top: 237px; width: 100%; text-align: center; font-size: 8px; color: var(--text-light); }
  .counter {
    position: absolute; left: 14px; right: 14px; height: 30px;
    display: flex; align-items: stretch; color: var(--white); font-size: 11px;
  }
  .counter span:first-child { flex: 1; padding-left: 8px; display: flex; align-items: center; }
  .counter span:last-child { width: 35px; display: flex; align-items: center; justify-content: center; }
  .counter--pending { top: 277px; background: var(--teal); }
  .counter--pending span:last-child { background: var(--teal-dark); color: #0e3b33; }
  .counter--sent { top: 314px; background: var(--blue); }
  .counter--sent span:last-child { background: var(--blue-dark); color: #0e2d3b; }

  /* Settings */
  .form { padding: 10px 14px 0; }
  .form label { display: block; font-size: 9px; color: var(--text); margin-bottom: 4px; }
  .field { height: 24px; background: var(--grey-field); margin-bottom: 10px; }
  .check-row { display: flex; justify-content: space-between; align-items: center; font-size: 9px; }
  .checkbox { width: 13px; height: 13px; background: var(--blue); display: flex; align-items: center; justify-content: center; }
  .checkbox--off { background: #cfcfcf; }

  /* Dimensions */
  .dim-group { padding: 6px 14px 0 14px; }
  .dim-head, .dim-item { display: flex; align-items: center; justify-content: space-between; }
  .dim-head { font-size: 10px; font-weight: 700; color: #444; height: 18px; }
  .dim-head .active { display: flex; align-items: center; gap: 6px; font-weight: 500; }
  .dim-item { font-size: 7.5px; color: var(--text-light); height: 17px; }
  .dim-label { display: flex; align-items: center; gap: 6px; }
  .add-row { display: flex; height: 22px; margin-top: 5px; }
  .add-row .field { flex: 1; height: 22px; margin: 0; }
  .add-row .add { width: 35px; background: var(--blue); color: var(--white); font-size: 7px; display: flex; align-items: center; justify-content: center; }

  /* Help */
  .group-bar { height: 24px; background: var(--grey-bar); font-size: 8px; font-weight: 500; color: #444; padding-left: 12px; display: flex; align-items: center; }
  .help-item {
    height: 28px; border-bottom: 1px solid #e5e5e5;
    display: flex; align-items: center; justify-content: space-between;
    padding: 0 12px; font-size: 8px; color: var(--text-light);
  }
  .go { width: 11px; height: 11px; border-radius: 50%; background: var(--red); display: flex; align-items: center; justify-content: center; }

  /* Scan */
  .scan-body { position: absolute; top: 33px; left: 0; right: 0; bottom: 0; background: #262626; }
  .viewfinder {
    position: absolute; left: 12px; top: 9px; width: 182px; height: 241px;
    border: 6px solid var(--red); background: #555;
    display: flex; align-items: center; justify-content: center; text-align: center;
    color: #b5b5b5; font-size: 10px; line-height: 1.3;
  }
  .scan-hint { position: absolute; top: 264px; width: 100%; text-align: center; font-size: 7px; color: #ddd; }
  .scan-footer { position: absolute; left: 0; right: 0; bottom: 0; height: 102px; background: var(--red); padding-top: 12px; }

  /* Receipts */
  .thumbs { display: flex; flex-wrap: wrap; gap: 10px; padding: 14px 14px 0; }
  .thumb {
    width: 52px; height: 62px; border: 3px solid var(--white);
    box-shadow: 0 0 0 1px #ddd;
    background: linear-gradient(135deg, #c9a777 0%, #e9e2d4 45%, #b8864f 100%);
  }
  .thumb--empty {
    background: #f0f0f0; border-bottom: 4px solid var(--red);
    font-size: 3.5px; color: #999; text-align: center; padding-top: 26px; line-height: 1.3; height: 80px;
  }
</style>
</head>
<body>

<!-- Row 1 -->
<section class="screen screen--splash" style="left:74px; top:120px;">
  <div class="splash-photo" role="img" aria-label="Close-up photograph of a printed receipt tinted red"></div>
  <div class="splash-brand">
    <div class="splash-name"><span class="mark"></span><span class="app-name">Slipvault</span></div>
    <div class="tagline">YOUR SMART SCANNER APP</div>
  </div>
</section>
<div class="caption" style="left:52px; top:565px;">Splash</div>

<section class="screen screen--main" style="left:325px; top:120px;">
  <header class="nav-bar">
    <div class="nav-left">
      <svg width="13" height="13" viewBox="0 0 13 13"><circle cx="6.5" cy="6.5" r="6.5" fill="#fff"/><rect x="5.7" y="5.5" width="1.6" height="4.5" fill="#e84c3d"/><circle cx="6.5" cy="3.7" r="1" fill="#e84c3d"/></svg>
    </div>
    <span class="app-name">Slipvault</span>
    <div class="nav-right">
      <svg width="12" height="10" viewBox="0 0 12 10"><rect y="0" width="12" height="2" fill="#fff"/><rect y="4" width="12" height="2" fill="#fff"/><rect y="8" width="12" height="2" fill="#fff"/></svg>
      <svg width="13" height="13" viewBox="0 0 24 24"><path fill="#fff" d="M19.4 13a7.5 7.5 0 0 0 0-2l2.1-1.6-2-3.5-2.5 1a7 7 0 0 0-1.7-1L15 3h-4l-.4 2.9a7 7 0 0 0-1.7 1l-2.5-1-2 3.5L6.6 11a7.5 7.5 0 0 0 0 2l-2.1 1.6 2 3.5 2.5-1a7 7 0 0 0 1.7 1L11 21h4l.4-2.9a7 7 0 0 0 1.7-1l2.5 1 2-3.5zM13 15.5a3.5 3.5 0 1 1 0-7 3.5 3.5 0 0 1 0 7z"/></svg>
    </div>
  </header>
  <div class="scan-button">START<br>SCANNING</div>
  <div class="status">READY</div>
  <div class="counter counter--pending"><span>Pending</span><span>12</span></div>
  <div class="counter counter--sent"><span>Sent</span><span>3</span></div>
</section>
<div class="caption" style="left:303px; top:565px;">Main * Revise</div>

<section class="screen screen--settings" style="left:577px; top:120px;">
  <header class="nav-bar">
    <div class="nav-left"><svg width="9" height="14" viewBox="0 0 9 14"><path d="M7.5 1.5 2 7l5.5 5.5" stroke="#fff" stroke-width="2.2" fill="none"/></svg></div>
    <span class="app-name">Slipvault</span>
  </header>
  <div class="section-bar">
    <svg width="10" height="10" viewBox="0 0 24 24"><path fill="#555" d="M19.4 13a7.5 7.5 0 0 0 0-2l2.1-1.6-2-3.5-2.5 1a7 7 0 0 0-1.7-1L15 3h-4l-.4 2.9a7 7 0 0 0-1.7 1l-2.5-1-2 3.5L6.6 11a7.5 7.5 0 0 0 0 2l-2.1 1.6 2 3.5 2.5-1a7 7 0 0 0 1.7 1L11 21h4l.4-2.9a7 7 0 0 0 1.7-1l2.5 1 2-3.5zM13 15.5a3.5 3.5 0 1 1 0-7 3.5 3.5 0 0 1 0 7z"/></svg>
    Settings
  </div>
  <div class="form">
    <label>User Name</label><div class="field"></div>
    <label>User Email</label><div class="field"></div>
    <label>Recipent Email</label><div class="field"></div>
    <div class="check-row">Save to Album Gallery?
      <span class="checkbox"><svg width="9" height="8" viewBox="0 0 9 8"><path d="M1 4l2.5 2.5L8 1" stroke="#fff" stroke-width="1.6" fill="none"/></svg></span>
    </div>
  </div>
  <div class="action-panel" style="height:144px;">
    <div class="btn btn--blue">Save</div>
    <div class="btn btn--teal">Close</div>
  </div>
</section>
<div class="caption" style="left:555px; top:565px;">Settings</div>

<section class="screen screen--dimensions" style="left:827px; top:120px;">
  <header class="nav-bar">
    <div class="nav-left"><svg width="9" height="14" viewBox="0 0 9 14"><path d="M7.5 1.5 2 7l5.5 5.5" stroke="#fff" stroke-width="2.2" fill="none"/></svg></div>
    <span class="app-name">Slipvault</span>
  </header>
  <div class="section-bar">
    <svg width="10" height="9" viewBox="0 0 10 9"><rect width="10" height="1.8" fill="#555"/><rect y="3.6" width="10" height="1.8" fill="#555"/><rect y="7.2" width="10" height="1.8" fill="#555"/></svg>
    Dimensions
  </div>
  <div class="dim-group">
    <div class="dim-head">
      <span class="dim-label"><svg width="8" height="8" viewBox="0 0 8 8"><path d="M1 7l1-3 4-4 2 2-4 4z" fill="#e84c3d"/></svg>Daily cost</span>
      <span class="active">Active <span class="checkbox"><svg width="9" height="8" viewBox="0 0 9 8"><path d="M1 4l2.5 2.5L8 1" stroke="#fff" stroke-width="1.6" fill="none"/></svg></span></span>
    </div>
    <div class="dim-item"><span class="dim-label"><svg width="7" height="7" viewBox="0 0 8 8"><path d="M1 7l1-3 4-4 2 2-4 4z" fill="#e84c3d"/></svg>Drink</span><svg width="8" height="8" viewBox="0 0 8 8"><path d="M1 1l6 6M7 1 1 7" stroke="#e84c3d" stroke-width="1.4"/></svg></div>
    <div class="dim-item"><span class="dim-label"><svg width="7" height="7" viewBox="0 0 8 8"><path d="M1 7l1-3 4-4 2 2-4 4z" fill="#e84c3d"/></svg>Snack</span><svg width="8" height="8" viewBox="0 0 8 8"><path d="M1 1l6 6M7 1 1 7" stroke="#e84c3d" stroke-width="1.4"/></svg></div>
    <div class="dim-item"><span class="dim-label"><svg width="7" height="7" viewBox="0 0 8 8"><path d="M1 7l1-3 4-4 2 2-4 4z" fill="#e84c3d"/></svg>Transport</span><svg width="8" height="8" viewBox="0 0 8 8"><path d="M1 1l6 6M7 1 1 7" stroke="#e84c3d" stroke-width="1.4"/></svg></div>
    <div class="add-row"><div class="field"></div><div class="add">ADD</div></div>
  </div>
  <div class="dim-group" style="padding-top:10px;">
    <div class="dim-head">
      <span class="dim-label"><svg width="8" height="8" viewBox="0 0 8 8"><path d="M1 7l1-3 4-4 2 2-4 4z" fill="#e84c3d"/></svg>Bill</span>
      <span class="active">Active <span class="checkbox checkbox--off"></span></span>
    </div>
    <div class="dim-item"><span class="dim-label"><svg width="7" height="7" viewBox="0 0 8 8"><path d="M1 7l1-3 4-4 2 2-4 4z" fill="#e84c3d"/></svg>Credit Card</span><svg width="8" height="8" viewBox="0 0 8 8"><path d="M1 1l6 6M7 1 1 7" stroke="#e84c3d" stroke-width="1.4"/></svg></div>
    <div class="add-row"><div class="field"></div><div class="add">ADD</div></div>
  </div>
  <div class="action-panel" style="height:138px;">
    <div class="btn btn--blue">Save</div>
    <div class="btn btn--teal">Close</div>
  </div>
</section>
<div class="caption" style="left:805px; top:565px;">Dimension * Revise</div>

<!-- Row 2 -->
<section class="screen screen--help" style="left:74px; top:683px;">
  <header class="nav-bar">
    <div class="nav-left"><svg width="9" height="14" viewBox="0 0 9 14"><path d="M7.5 1.5 2 7l5.5 5.5" stroke="#fff" stroke-width="2.2" fill="none"/></svg></div>
    <span class="app-name">Slipvault</span>
  </header>
  <div class="section-bar" style="background:#f4f4f4;">
    <svg width="10" height="10" viewBox="0 0 13 13"><circle cx="6.5" cy="6.5" r="6.5" fill="#555"/><rect x="5.7" y="5.5" width="1.6" height="4.5" fill="#fff"/><circle cx="6.5" cy="3.7" r="1" fill="#fff"/></svg>
    Help
  </div>
  <div class="group-bar">About</div>
  <div class="help-item">Tutorial<span class="go"><svg width="5" height="6" viewBox="0 0 5 6"><path d="M1 .5 3.5 3 1 5.5" stroke="#fff" stroke-width="1.2" fill="none"/></svg></span></div>
  <div class="help-item">FAQ<span class="go"><svg width="5" height="6" viewBox="0 0 5 6"><path d="M1 .5 3.5 3 1 5.5" stroke="#fff" stroke-width="1.2" fill="none"/></svg></span></div>
  <div class="help-item">Getting Started<span class="go"><svg width="5" height="6" viewBox="0 0 5 6"><path d="M1 .5 3.5 3 1 5.5" stroke="#fff" stroke-width="1.2" fill="none"/></svg></span></div>
  <div class="help-item">Manage Subsciption<span class="go"><svg width="5" height="6" viewBox="0 0 5 6"><path d="M1 .5 3.5 3 1 5.5" stroke="#fff" stroke-width="1.2" fill="none"/></svg></span></div>
  <div class="group-bar">More Info</div>
  <div class="help-item">Terms of Service<span class="go"><svg width="5" height="6" viewBox="0 0 5 6"><path d="M1 .5 3.5 3 1 5.5" stroke="#fff" stroke-width="1.2" fill="none"/></svg></span></div>
  <div class="help-item">Privacy Policy<span class="go"><svg width="5" height="6" viewBox="0 0 5 6"><path d="M1 .5 3.5 3 1 5.5" stroke="#fff" stroke-width="1.2" fill="none"/></svg></span></div>
  <div class="help-item">Official Website<span class="go"><svg width="5" height="6" viewBox="0 0 5 6"><path d="M1 .5 3.5 3 1 5.5" stroke="#fff" stroke-width="1.2" fill="none"/></svg></span></div>
  <div class="help-item">About Developer<span class="go"><svg width="5" height="6" viewBox="0 0 5 6"><path d="M1 .5 3.5 3 1 5.5" stroke="#fff" stroke-width="1.2" fill="none"/></svg></span></div>
</section>
<div class="caption" style="left:52px; top:1130px;">Help</div>

<section class="screen screen--scan" style="left:325px; top:683px;">
  <header class="nav-bar">
    <div class="nav-left"><svg width="9" height="14" viewBox="0 0 9 14"><path d="M7.5 1.5 2 7l5.5 5.5" stroke="#fff" stroke-width="2.2" fill="none"/></svg></div>
    <span class="app-name">Slipvault</span>
  </header>
  <div class="scan-body">
    <div class="viewfinder">SOME<br>RECEIPT<br>IMAGE<br>TO SCAN</div>
    <div class="scan-hint">TAP SCREEN TO SCAN</div>
    <div class="scan-footer"><div class="btn btn--teal">Close</div></div>
  </div>
</section>
<div class="caption" style="left:303px; top:1130px;">Scan * Revise</div>

<section class="screen screen--pending" style="left:577px; top:683px;">
  <header class="nav-bar">
    <div class="nav-left"><svg width="9" height="14" viewBox="0 0 9 14"><path d="M7.5 1.5 2 7l5.5 5.5" stroke="#fff" stroke-width="2.2" fill="none"/></svg></div>
    <span class="app-name">Slipvault</span>
  </header>
  <div class="section-bar">
    <svg width="10" height="9" viewBox="0 0 10 9"><rect width="7" height="9" fill="none" stroke="#555" stroke-width="1.4"/><path d="M7 4.5h3" stroke="#555" stroke-width="1.4"/></svg>
    Pending Receipts
  </div>
  <div class="thumbs">
    <div class="thumb" role="img" aria-label="Photo of a scanned receipt"></div>
    <div class="thumb" role="img" aria-label="Photo of a scanned receipt"></div>
    <div class="thumb" role="img" aria-label="Photo of a scanned receipt"></div>
    <div class="thumb thumb--empty">ADD<br>RECEIPT TO REVIEW</div>
  </div>
  <div class="action-panel" style="height:178px; background:var(--white);">
    <div class="btn btn--blue">Send All</div>
    <div class="btn btn--red">Delete All</div>
    <div class="btn btn--teal">Close</div>
  </div>
</section>
<div class="caption" style="left:555px; top:1130px;">Pending * Revise</div>

<section class="screen screen--sent" style="left:827px; top:683px;">
  <header class="nav-bar">
    <div class="nav-left"><svg width="9" height="14" viewBox="0 0 9 14"><path d="M7.5 1.5 2 7l5.5 5.5" stroke="#fff" stroke-width="2.2" fill="none"/></svg></div>
    <span class="app-name">Slipvault</span>
  </header>
  <div class="section-bar">
    <svg width="10" height="9" viewBox="0 0 10 9"><rect width="7" height="9" fill="none" stroke="#555" stroke-width="1.4"/><path d="M7 4.5h3" stroke="#555" stroke-width="1.4"/></svg>
    Sent Receipts
  </div>
  <div class="thumbs">
    <div class="thumb" role="img" aria-label="Photo of a sent receipt"></div>
    <div class="thumb" role="img" aria-label="Photo of a sent receipt"></div>
    <div class="thumb" role="img" aria-label="Photo of a sent receipt"></div>
  </div>
  <div class="action-panel" style="height:140px; background:var(--white);">
    <div class="btn btn--red">Delete All</div>
    <div class="btn btn--teal">Close</div>
  </div>
</section>
<div class="caption" style="left:805px; top:1130px;">Sent * Revise</div>

</body>
</html>
```